Whitepaper: 7 Keys to Achieving Success of Your RTLS Initiative

Create a graphical layout for a whitepaper that would include 7 illustrations matching each subject line. Colors aligned with Boundless Stride branding guide (attached)

Just to summarize, I would need graphics/illustrations for 7 bullet points - Key #1: Set Measurements for Success Key #2: Establish a Clear Roadmap Key #3: Don’t Use Pilots (small try out of software) Key #4: Plan for the Future, from the Start Key #5: Think about RTLS as an Initiative, not a Project Key #6: Nurture the Change Key #7: Show Successes, Early

I would expect about 2-3 illustrations per page. Format - US size 8.5x11. PDF file, but would like to have the ability to edit text if needed. Thank you for your interest. Colors don't need to match the branding. It is a healthcare whitepaper so it could be blue and green.

Reason: Some of you have asked for a time extension.

```html
<!DOCTYPE html>
<html lang="en">
<head>
<meta charset="utf-8">
<title>7 Keys to Achieving Success of Your RTLS Initiative</title>
<link rel="stylesheet" href="https://fonts.googleapis.com/css2?family=Raleway:wght@300;400;700&family=Source+Sans+3:wght@300;400;700&display=swap">
<style>
  :root {
    --backdrop: #fcefc8;
    --paper: #ffffff;
    --ink: #3d3d47;
    --ink-soft: #4a4a52;
    --coral: #ec5f5f;
    --coral-deep: #c9454b;
    --rule: #8a8a90;
    --placeholder: #e6e6ea;
  }
  * { box-sizing: border-box; margin: 0; padding: 0; }
  html, body { width: 900px; height: 1200px; overflow: hidden; }
  body { background: var(--backdrop); position: relative; font-family: "Raleway", sans-serif; color: var(--ink); }

  .page {
    position: absolute; left: 55px; top: 50px; width: 790px; height: 1025px;
    background: var(--paper); box-shadow: 4px 5px 6px rgba(0,0,0,.22);
    overflow: hidden;
  }
  .abs { position: absolute; }

  .number-badge {
    left: 155px; top: 50px; width: 122px; height: 122px; border-radius: 50%;
    background: var(--coral); color: #fff;
    font: 700 88px/122px "Source Sans 3", sans-serif; text-align: center;
  }
  .headline {
    left: 285px; top: 70px;
    font: 700 29px/37px "Source Sans 3", sans-serif; color: var(--ink);
  }

  .author-photo {
    left: 73px; top: 166px; width: 68px; height: 68px; border-radius: 50%;
    border: 2px solid #bcbcc2;
    background: radial-gradient(circle at 50% 45%, #b98f7d, #7c6a66 70%, #5a5a62);
  }
  .author-name { left: 151px; top: 182px; font: 700 17px/20px "Source Sans 3", sans-serif; }
  .author-role { left: 151px; top: 203px; font: 700 14px/18px "Source Sans 3", sans-serif; }

  .intro {
    left: 73px; width: 648px;
    font: 300 14.2px/19px "Source Sans 3", sans-serif; color: var(--ink-soft);
    text-align: justify; letter-spacing: -0.1px;
  }
  .intro-first { top: 241px; }
  .intro-second { top: 316px; }

  .divider { left: 0; top: 409px; width: 790px; height: 1px; background: var(--rule); }

  .key-pill {
    left: 318px; width: 139px; height: 40px; border-radius: 14px;
    color: #fff; font: 700 20px/40px "Raleway", sans-serif; text-align: center;
  }
  .key-pill.first { top: 387px; background: var(--coral-deep); }
  .key-pill.second { top: 682px; background: var(--ink); z-index: 2; }

  .key-illustration { border-radius: 6px; }
  .ruler-art { left: 70px; top: 425px; width: 225px; height: 245px; background: linear-gradient(135deg, #f3f3f5, var(--placeholder)); }

  .key-title { font: 700 17.5px/21px "Raleway", sans-serif; }
  .key-body { font: 400 14.6px/18.7px "Raleway", sans-serif; text-align: justify; }
  .key-one .key-title { left: 328px; top: 449px; color: var(--ink); }
  .key-one .key-body { left: 328px; top: 467px; width: 391px; color: var(--ink-soft); }

  .band { left: 0; top: 0; }
  .key-two .key-title { left: 73px; top: 727px; width: 300px; color: #fff; }
  .key-two .key-body { left: 73px; top: 771px; width: 391px; color: #fff; font-weight: 300; }
  .roadmap-card {
    left: 482px; top: 720px; width: 308px; height: 206px; background: var(--paper);
    border-radius: 16px 0 0 16px;
  }
  .roadmap-art { left: 20px; top: 18px; width: 260px; height: 170px; background: linear-gradient(135deg, #f3f3f5, var(--placeholder)); }
</style>
</head>
<body>
  <main class="page">
    <div class="abs number-badge">7</div>
    <h1 class="abs headline">Keys to Achieving Success<br>of Your RTLS Initiative</h1>

    <div class="abs author-photo" role="img" aria-label="Portrait photo of the author"></div>
    <p class="abs author-name">by Dr. Martin Vale,</p>
    <p class="abs author-role">Chief Medical Informatics Officer | Riverbend Pediatric Health Network</p>

    <p class="abs intro intro-first">In my role as CMIO, part of my job is to identify new technologies that are going to be of value to our organization, but also to create the environment in which we can be successful in implementing these technologies, and truly utilizing them to the benefit of our patients, our care providers, and our organization.</p>
    <p class="abs intro intro-second">In this article, I am sharing my key learnings to achieving success with Real-Time Location Systems (RTLS), which I implemented in various healthcare institutions for which I have had the privilege to work.</p>

    <div class="abs divider"></div>
    <div class="abs key-pill first">Key #1</div>

    <section class="key-one">
      <div class="abs key-illustration ruler-art" role="img" aria-label="Illustration: RTLS label with green tick above a ruler marked 1 to 4 years"></div>
      <h2 class="abs key-title">Set Measurements for RTLS Success</h2>
      <p class="abs key-body">You cannot claim a success if you don't define what success means to your organization. You need to work with your executive team to establish a clear vision of what RTLS is going to do for you and agree on the expected return on investment (ROI) for this technology. I have to add that as someone who is a part of the executive team myself, I don't really care how much something costs. What I care about is how much value does it bring back to the organization for that cost.</p>
    </section>

    <section class="key-two">
      <svg class="abs band" width="790" height="1025" aria-hidden="true">
        <polygon points="0,740 63,702 790,702 790,945 0,945" fill="var(--coral)"/>
      </svg>
      <div class="abs key-pill second">Key #2</div>
      <h2 class="abs key-title">Establish a Clear Roadmap for an RTLS Deployment</h2>
      <p class="abs key-body">It is not uncommon that you will come up with 10, 50, or even 100 different projects and problems that can be solved with RTLS technology. However, in order to actually act on all of those opportunities you really need a clear roadmap of which use cases and in what particular order you want to implement them to get the fastest ROI and the best utilization of your resources.</p>
      <div class="abs roadmap-card">
        <div class="abs key-illustration roadmap-art" role="img" aria-label="Illustration: zigzag deployment path with location pin, labelled RTS Deployment and Fastest ROI"></div>
      </div>
    </section>
  </main>
</body>
</html>
```